Cedar Hollow at Pine Basin Marketing Sign

I need a sign designed that will be 4'X8'. You designed another sign for me not too long ago - Fernridge at Harlow's Point. I need another sign similar in layout, but with the Cedar Hollow logo, tagline, rendering, colors, etc.

Attached is the logo, and rendering. Here are the other items I need to have on this sign:
Tagline - Life Outside The Lines
JOIN OUR WAITLIST TODAY!
Move-In Beginning Summer 2017
www.cedarhollowhomesx.com

```html
<!DOCTYPE html>
<html lang="en">
<head>
<meta charset="utf-8">
<title>Cedar Hollow at Pine Basin – Marketing Sign</title>
<link href="https://fonts.googleapis.com/css2?family=Quicksand:wght@500&family=Montserrat:wght@600;700;800&family=Yellowtail&display=swap" rel="stylesheet">
<style>
  :root {
    --backdrop: #000000;
    --sign-white: #ffffff;
    --teal: #2a9dbd;
    --brand-blue: #2f75a6;
    --rule-blue: #2b5f9a;
    --ink: #333333;
    --tagline-yellow: #f5d21f;
  }
  * { margin: 0; padding: 0; box-sizing: border-box; }
  html, body {
    width: 724px; height: 1200px; overflow: hidden;
    background: var(--backdrop);
  }
  .sign {
    position: absolute; left: 93px; top: 62px;
    width: 538px; height: 1076px;
    background: var(--sign-white);
    font-family: "Montserrat", Arial, sans-serif;
  }
  .brand {
    position: absolute; top: 42px; left: 0; width: 100%;
    text-align: center;
  }
  .brand-square {
    display: block; margin: 0 auto;
    width: 93px; height: 104px;
    border: 4px solid var(--brand-blue);
  }
  .brand-name {
    font-family: "Quicksand", Arial, sans-serif; font-weight: 500;
    color: var(--teal);
    font-size: 33px; line-height: 1; margin-top: 18px;
    letter-spacing: 0.5px;
  }
  .brand-place {
    font-family: "Quicksand", Arial, sans-serif; font-weight: 500;
    color: var(--teal);
    font-size: 16px; line-height: 1; margin-top: 3px;
  }
  .brand-rule {
    width: 257px; height: 2px; margin: 5px auto 0;
    background: var(--rule-blue);
  }
  .brand-descriptor {
    font-family: "Montserrat", Arial, sans-serif; font-weight: 600;
    color: var(--ink);
    font-size: 10.5px; letter-spacing: 2.6px; margin-top: 6px;
  }
  .rendering {
    position: absolute; left: 0; top: 246px;
    width: 538px; height: 447px;
    background:
      linear-gradient(180deg, #ffffff 0%, #dfe8ef 10%, #c9d3d9 30%, #c8b7a3 55%, #8e8a96 72%, #5c5868 88%, #4d4a33 100%);
  }
  .tagline {
    position: absolute; left: 0; top: 634px; width: 538px;
    text-align: center;
    font-family: "Yellowtail", cursive;
    color: var(--tagline-yellow);
    font-size: 38px; line-height: 1;
  }
  .cta-lead {
    position: absolute; top: 726px; left: 0; width: 100%;
    text-align: center; color: var(--brand-blue);
    font-weight: 800; font-size: 36px; line-height: 1;
    letter-spacing: -0.3px;
  }
  .cta-main {
    position: absolute; top: 762px; left: 0; width: 100%;
    text-align: center; color: var(--brand-blue);
    font-weight: 800; font-size: 96px; line-height: 1;
    letter-spacing: -3px;
  }
  .move-in {
    position: absolute; left: 91px; top: 868px;
    width: 357px; height: 93px;
    border: 2px solid var(--brand-blue);
    display: flex; align-items: center; justify-content: center;
    text-align: center; color: var(--teal);
    font-weight: 800; font-size: 25px; line-height: 1.25;
  }
  .web-band {
    position: absolute; left: 0; bottom: 0;
    width: 100%; height: 77px;
    background: var(--brand-blue);
    display: flex; align-items: center; justify-content: center;
    color: var(--sign-white);
    font-weight: 700; font-size: 29px;
  }
</style>
</head>
<body>
  <main class="sign">
    <header class="brand">
      <span class="brand-square"></span>
      <p class="brand-name">CEDAR HOLLOW</p>
      <p class="brand-place">at Pine Basin</p>
      <div class="brand-rule"></div>
      <p class="brand-descriptor">APARTMENT HOMES</p>
    </header>

    <div class="rendering" role="img" aria-label="Watercolor architectural rendering of three-story craftsman-style apartment buildings with trees, a parking lot and parked cars"></div>
    <p class="tagline">Life Outside The Lines</p>

    <h1 class="cta-lead">JOIN OUR WAITLIST</h1>
    <p class="cta-main">TODAY!</p>

    <div class="move-in">MOVE-IN BEGINNING<br>SUMMER 2017</div>

    <footer class="web-band">www.cedarhollowhomesx.com</footer>
  </main>
</body>
</html>
```